Web Design for Harbor Ledger Allies

Harbor Ledger Allies needs the photoshop files for a simple, clean and professional website design. The company is building a network of bookkeepers/accountants to handle outsourced bookkeeping services for start ups and small businesses. It needs to both attract bookkeepers to become partners and give clients confidence in the professional network. The partners will use products like Tallymint Web, Brightfolio.example and PennyTrim.example for start ups, as well as help with tasks using the clients existing accounting software.

A home and subpage design is needed. I'll award the work based on the home design. The minor subpage changes can be worked out in the workroom stage.

The pages for the navigation will be: Home, Services, Locations, Partners, FAQ, Contact

```html
<!DOCTYPE html>
<html lang="en">
<head>
<meta charset="utf-8">
<title>Harbor Ledger Allies</title>
<link rel="stylesheet" href="https://fonts.googleapis.com/css2?family=Roboto:wght@300;400;500;700&display=swap">
<style>
:root{
  --blue:#1b9be0;
  --blue-deep:#1689c8;
  --footer:#1a9ad9;
  --ink:#555a60;
  --muted:#8c9196;
  --line:#dcdfe2;
  --bar:#c9cdd1;
  --card-border:#dfe2e5;
  --white:#ffffff;
}
*{box-sizing:border-box;margin:0;padding:0}
html,body{width:854px;height:1200px;overflow:hidden;background:var(--white)}
body{position:relative;font-family:"Roboto",Arial,sans-serif;color:var(--ink)}
.abs{position:absolute}

/* header */
.brand{left:98px;top:24px;display:flex;align-items:center;gap:8px}
.brand-mark{width:14px;height:14px;background:var(--blue);border-radius:50%}
.brand-name{font-size:13px;font-weight:500;color:var(--blue);line-height:13px;text-transform:uppercase;letter-spacing:.3px}
.auth-btn{top:34px;height:18px;background:var(--blue);color:var(--white);font-size:9px;display:flex;align-items:center;justify-content:center;text-transform:uppercase}
.login{left:635px;width:51px}
.logout{left:694px;width:61px}

/* navigation */
.main-nav{left:98px;top:86px;width:657px;height:35px;background:var(--blue);display:flex;align-items:center;padding-left:19px}
.nav-item{color:var(--white);font-size:10.5px;padding:0 20px;border-left:1px solid rgba(255,255,255,.35);line-height:12px}
.nav-item:first-child{padding-left:0;border-left:none;padding-right:20px}
.search{left:580px;top:93px;width:169px;height:21px;background:var(--blue-deep);display:flex;align-items:center;justify-content:space-between;padding:0 6px;font-size:8.5px;color:rgba(255,255,255,.6)}

/* hero */
.hero{left:98px;top:141px;width:657px;height:229px;background:linear-gradient(120deg,#3b3735 0%,#8a8580 40%,#d6d2cc 60%,#6b5a4c 100%);border:1px solid var(--card-border)}
.hero-caption{left:341px;top:211px;width:352px;height:85px;background:rgba(40,40,40,.82);padding:16px 30px 0 25px}
.hero-title{font-size:26px;font-weight:500;color:var(--white);line-height:28px}
.hero-sub{font-size:19px;font-weight:500;color:var(--blue);text-align:right;line-height:24px}
.dots{left:670px;top:346px;display:flex;gap:3px}
.dot{width:11px;height:11px;border-radius:50%;background:#555}
.dot.active{background:var(--blue)}

/* section headings */
.sec-head{height:16px;font-size:13px;color:var(--ink);line-height:16px}
.sec-rule{height:2px;background:var(--line)}
.sec-rule::before{content:"";position:absolute;left:0;top:0;height:2px;width:var(--w);background:var(--bar)}
.go{width:12px;height:12px}

/* cards */
.card{border:1px solid var(--card-border);background:var(--white)}
.thumb{position:absolute}
.body-text{font-size:8.8px;line-height:11px;color:var(--muted);font-weight:300}
.link{color:var(--blue)}

.news-item{position:absolute;left:14px;width:175px}
.news-title{font-size:10.5px;color:var(--blue);text-decoration:underline;display:flex;align-items:center;gap:6px}
.news-title::before{content:"";width:5px;height:5px;border-radius:50%;background:#555}
.read-more{font-size:8.8px;color:var(--ink);text-decoration:underline;text-align:right;margin-top:9px}
.divider{position:absolute;left:14px;width:175px;height:1px;background:var(--line)}

.gallery-cap{position:absolute;font-size:8.8px;text-decoration:underline;color:var(--ink);text-align:center;width:91px}

.partner-name{position:absolute;top:0;height:73px;display:flex;align-items:center;font-size:22px;font-weight:500;color:#4a4f55}

/* footer */
.footer{left:0;top:1038px;width:854px;height:162px;background:var(--footer)}
.news-head{left:98px;top:1066px;font-size:13px;font-weight:500;color:var(--white)}
.news-rule{left:98px;top:1088px;width:657px;height:1px;background:rgba(255,255,255,.3)}
.news-rule::before{content:"";position:absolute;left:0;top:0;width:150px;height:2px;background:rgba(255,255,255,.5)}
.field{top:1102px;height:25px;background:var(--blue-deep);border:1px solid rgba(0,0,0,.08);font-size:8.5px;color:rgba(255,255,255,.5);padding:7px 6px}
.submit{left:581px;top:1103px;width:174px;height:24px;background:var(--white);color:var(--ink);font-size:10px;display:flex;align-items:center;justify-content:center}
.copyright{left:0;top:1158px;width:854px;text-align:center;font-size:8.5px;color:var(--white)}
</style>
</head>
<body>

<svg width="0" height="0" style="position:absolute">
  <defs>
    <symbol id="go" viewBox="0 0 12 12">
      <circle cx="6" cy="6" r="6" fill="#1b9be0"/>
      <path d="M5 3.5 L7.5 6 L5 8.5" fill="none" stroke="#fff" stroke-width="1.5"/>
    </symbol>
    <symbol id="go-light" viewBox="0 0 12 12">
      <circle cx="6" cy="6" r="6" fill="#fff"/>
      <path d="M5 3.5 L7.5 6 L5 8.5" fill="none" stroke="#1a9ad9" stroke-width="1.5"/>
    </symbol>
  </defs>
</svg>

<header>
  <div class="abs brand">
    <span class="brand-mark"></span>
    <span class="brand-name">Harbor Ledger<br>Allies</span>
  </div>
  <div class="abs auth-btn login">Log In</div>
  <div class="abs auth-btn logout">Log Out</div>
</header>

<nav class="abs main-nav">
  <span class="nav-item">Home</span>
  <span class="nav-item">Services</span>
  <span class="nav-item">Locations</span>
  <span class="nav-item">Partners</span>
  <span class="nav-item">FAQ</span>
  <span class="nav-item">Cantact Us</span>
</nav>
<div class="abs search">
  <span>Enter your keywords</span>
  <svg width="13" height="13" viewBox="0 0 13 13"><circle cx="5.5" cy="5.5" r="4.2" fill="none" stroke="#fff" stroke-width="1.5"/><path d="M8.5 8.5 L12 12" stroke="#fff" stroke-width="1.6"/></svg>
</div>

<section>
  <div class="abs hero" role="img" aria-label="Photo of a hand with a red pencil working on a calculator over financial papers"></div>
  <div class="abs hero-caption">
    <div class="hero-title">FAITHFUL ACCOUNTING</div>
    <div class="hero-sub">FOR OUR CLIENTS</div>
  </div>
  <div class="abs dots"><span class="dot"></span><span class="dot"></span><span class="dot active"></span><span class="dot"></span><span class="dot"></span></div>
</section>

<!-- feature columns -->
<section>
  <div class="abs sec-head" style="left:98px;top:401px">Accounting Approach</div>
  <svg class="abs go" style="left:286px;top:403px"><use href="#go"/></svg>
  <div class="abs sec-rule" style="left:98px;top:420px;width:201px;--w:137px"></div>

  <div class="abs sec-head" style="left:325px;top:401px">Lorem Ipsum is simply</div>
  <svg class="abs go" style="left:514px;top:403px"><use href="#go"/></svg>
  <div class="abs sec-rule" style="left:325px;top:420px;width:201px;--w:138px"></div>

  <div class="abs sec-head" style="left:553px;top:401px">Lorem Ipsum is simply</div>
  <svg class="abs go" style="left:742px;top:403px"><use href="#go"/></svg>
  <div class="abs sec-rule" style="left:553px;top:420px;width:202px;--w:138px"></div>

  <div class="abs card" style="left:98px;top:441px;width:201px;height:177px">
    <div class="thumb" style="left:13px;top:13px;width:175px;height:75px;background:linear-gradient(110deg,#2e2e2e,#b8b4ae 55%,#d9d6d0)" role="img" aria-label="Photo of a calculator and pen on a spreadsheet"></div>
    <p class="abs body-text" style="left:13px;top:104px;width:178px">Lorem Ipsum is simply dummy text of the printing and typesetting industry. Lorem Ipsum has been the industry's standard dummy text ever since the 1500s, when an unknown printer took a galley of type and scrambled it to make a type.</p>
  </div>
  <div class="abs card" style="left:325px;top:441px;width:201px;height:177px">
    <div class="thumb" style="left:13px;top:13px;width:175px;height:75px;background:linear-gradient(110deg,#e9e6e2,#a99a8a 45%,#4c4a48)" role="img" aria-label="Photo of business colleagues reviewing documents at a table"></div>
    <p class="abs body-text" style="left:13px;top:104px;width:178px">Lorem Ipsum is simply dummy text of the printing and typesetting industry. Lorem Ipsum has been the industry's standard dummy text ever since the 1500s, when an unknown printer took a galley of type and scrambled it to make a type.</p>
  </div>
  <div class="abs card" style="left:553px;top:441px;width:202px;height:177px">
    <div class="thumb" style="left:13px;top:13px;width:175px;height:75px;background:linear-gradient(110deg,#2e2e2e,#b8b4ae 55%,#d9d6d0)" role="img" aria-label="Photo of a calculator and pen on a spreadsheet"></div>
    <p class="abs body-text" style="left:13px;top:104px;width:178px">Lorem Ipsum is simply dummy text of the printing and typesetting industry. Lorem Ipsum has been the industry's standard dummy text ever since the 1500s, when an unknown printer took a galley of type and scrambled it to make a type.</p>
  </div>
</section>

<!-- news and refund -->
<section>
  <div class="abs sec-head" style="left:98px;top:648px">Hot News</div>
  <svg class="abs go" style="left:286px;top:651px"><use href="#go"/></svg>
  <div class="abs sec-rule" style="left:98px;top:668px;width:201px;--w:65px"></div>

  <div class="abs sec-head" style="left:325px;top:648px">Easily Gets you the Maximum Refund</div>
  <svg class="abs go" style="left:742px;top:651px"><use href="#go"/></svg>
  <div class="abs sec-rule" style="left:325px;top:668px;width:430px;--w:229px"></div>

  <div class="abs card" style="left:98px;top:689px;width:201px;height:179px">
    <div class="news-item" style="top:14px">
      <div class="news-title">Lorem Ipsum is simply</div>
      <p class="body-text" style="margin-top:6px">Lorem Ipsum is simply dummy text of the printing and typesetting industry.</p>
      <div class="read-more">Read More</div>
    </div>
    <div class="divider" style="top:86px"></div>
    <div class="news-item" style="top:104px">
      <div class="news-title">Lorem Ipsum is simply</div>
      <p class="body-text" style="margin-top:6px">Lorem Ipsum is simply dummy text of the printing and typesetting industry.</p>
      <div class="read-more">Read More</div>
    </div>
  </div>

  <div class="abs card" style="left:325px;top:689px;width:430px;height:179px">
    <p class="abs body-text" style="left:13px;top:12px;width:400px">Lorem Ipsum is simply dummy text of <span class="link">the printing and typesetting industry</span>. Lorem Ipsum has been the industry's standard dummy text ever&nbsp; unknown printer took a galley of type.</p>
    <p class="abs body-text" style="left:13px;top:45px;width:400px">Lorem Ipsum is simply dummy text of the printing and typesetting industry. Lorem Ipsum has been the industry's standard <span class="link">dummy text ever&nbsp; unknown printer took a galley of type</span>..</p>
    <div class="thumb" style="left:13px;top:83px;width:91px;height:67px;background:linear-gradient(180deg,#f1f1f1,#8d8f93)" role="img" aria-label="Photo of a business team standing together"></div>
    <div class="thumb" style="left:116px;top:83px;width:91px;height:67px;background:linear-gradient(180deg,#d8dde3,#5c6168)" role="img" aria-label="Photo of a meeting in front of a chart on a screen"></div>
    <div class="thumb" style="left:220px;top:83px;width:91px;height:67px;background:linear-gradient(160deg,#3a3a3a,#c9c4bc)" role="img" aria-label="Photo of a desk phone and paperwork"></div>
    <div class="thumb" style="left:323px;top:83px;width:91px;height:67px;background:linear-gradient(160deg,#e6e6e6,#4d4f52)" role="img" aria-label="Photo of a woman working through documents at a desk"></div>
    <div class="gallery-cap" style="left:13px;top:158px">Lorem Ipsum is</div>
    <div class="gallery-cap" style="left:116px;top:158px">Lorem Ipsum is</div>
    <div class="gallery-cap" style="left:220px;top:158px">Lorem Ipsum is</div>
    <div class="gallery-cap" style="left:323px;top:158px">Lorem Ipsum is</div>
  </div>
</section>

<!-- partners -->
<section>
  <div class="abs sec-head" style="left:98px;top:899px">Our Partner</div>
  <svg class="abs go" style="left:742px;top:902px"><use href="#go"/></svg>
  <div class="abs sec-rule" style="left:98px;top:919px;width:657px;--w:77px"></div>

  <div class="abs card" style="left:98px;top:941px;width:657px;height:73px">
    <div class="abs" style="left:20px;top:12px;width:50px;height:50px;background:#6d7075;border-radius:6px" role="img" aria-label="Tallymint Web partner badge"></div>
    <div class="partner-name" style="left:130px;font-size:19px">Brightfolio</div>
    <div class="partner-name" style="left:330px">Northwise</div>
    <div class="partner-name" style="left:500px">Pinecrest Pay</div>
  </div>
</section>

<footer>
  <div class="abs footer"></div>
  <div class="abs news-head">Sing Up For News Letter</div>
  <svg class="abs go" style="left:742px;top:1070px"><use href="#go-light"/></svg>
  <div class="abs news-rule"></div>
  <div class="abs field" style="left:98px;width:233px">Enter your Name</div>
  <div class="abs field" style="left:339px;width:234px">Enter your E-Mail</div>
  <div class="abs submit">Submit</div>
  <div class="abs copyright">Copyright 2014 Harbor Ledger Allies. All Rights Reserved</div>
</footer>

</body>
</html>
```